Construction Company

Design a clutter free business card, it can be double-sided utilizing the logo for BNX Ltd simple with all relevant contact information.

Please also a letterhead design to function for the purposes of invoicing, all mail requirements, with header to be distinctive while the footer ties page together and incorporates all necessary information.

For now, please use generic / dummy text and when a winner is selected, I will disclose the contact information.

Hi Designers! Please read the updated brief which includes the design of a business card and letterhead. Thank you!

```html
<!DOCTYPE html>
<html lang="en">
<head>
<meta charset="utf-8">
<title>BNX Ltd – Business Card</title>
<link rel="stylesheet" href="https://fonts.googleapis.com/css2?family=Playfair+Display:wght@700&family=Roboto:wght@400;500&display=swap">
<style>
  :root {
    --navy: #22388f;
    --navy-deep: #14286f;
    --gold: #bf9a2c;
    --paper: #ffffff;
    --ink-grey: #555b66;
    --backdrop: #d9d8d5;
  }
  * { margin: 0; padding: 0; box-sizing: border-box; }
  html, body { width: 1200px; height: 801px; overflow: hidden; }
  body {
    background: var(--backdrop);
    font-family: "Roboto", Arial, sans-serif;
    position: relative;
  }
  .card {
    position: absolute;
    top: 257px;
    width: 500px;
    height: 286px;
    border: 2px solid var(--gold);
    overflow: hidden;
    box-shadow: 0 10px 24px rgba(0,0,0,0.18);
  }
  .card--front { left: 60px; background: var(--paper); }
  .card--back {
    left: 640px;
    background: linear-gradient(160deg, var(--navy) 0%, var(--navy-deep) 100%);
    display: flex; align-items: center; justify-content: center;
  }
  .brand-name {
    font-family: "Playfair Display", Georgia, serif;
    font-weight: 700;
    white-space: nowrap;
  }
  .card--front .brand-name {
    position: absolute; left: 40px; top: 92px;
    font-size: 40px; color: var(--navy);
  }
  .card--back .brand-name { font-size: 62px; color: var(--paper); margin-top: -10px; }
  .divider {
    position: absolute; left: 232px; top: 62px;
    width: 1.5px; height: 112px; background: var(--navy);
  }
  .contact { position: absolute; left: 256px; top: 54px; }
  .contact__name {
    font-family: "Playfair Display", Georgia, serif;
    font-weight: 700; font-size: 19px; color: var(--navy); letter-spacing: 0.5px;
  }
  .contact__role { font-weight: 500; font-size: 14px; color: var(--gold); margin-top: 2px; }
  .contact__list { list-style: none; margin-top: 14px; }
  .contact__list li {
    display: flex; align-items: center; gap: 8px;
    font-size: 14px; color: var(--ink-grey); line-height: 22px;
  }
  .contact__list svg { width: 13px; height: 13px; flex: none; fill: var(--navy); }
  .address-band {
    position: absolute; left: 0; bottom: 26px;
    width: 440px; height: 26px; background: var(--navy);
    display: flex; align-items: center; gap: 8px; padding-left: 30px;
    color: var(--paper); font-size: 13.5px; letter-spacing: 0.3px;
  }
  .address-band svg { width: 11px; height: 14px; fill: var(--paper); }
  .accent-corner {
    position: absolute; right: 0; bottom: 44px;
    width: 70px; height: 22px; background: var(--gold);
  }
</style>
</head>
<body>
  <section class="card card--front">
    <div class="brand-name">BNX Ltd</div>
    <div class="divider"></div>
    <div class="contact">
      <div class="contact__name">MARK ELLISON</div>
      <div class="contact__role">Director</div>
      <ul class="contact__list">
        <li><svg viewBox="0 0 24 24"><path d="M6.6 10.8a15 15 0 0 0 6.6 6.6l2.2-2.2a1 1 0 0 1 1-.25 11.4 11.4 0 0 0 3.6.57 1 1 0 0 1 1 1V20a1 1 0 0 1-1 1A17 17 0 0 1 3 4a1 1 0 0 1 1-1h3.5a1 1 0 0 1 1 1c0 1.25.2 2.45.57 3.6a1 1 0 0 1-.25 1z"/></svg>555.204.7788</li>
        <li><svg viewBox="0 0 24 24"><path d="M2 5h20v14H2z M3.5 6.5 12 13l8.5-6.5" fill="none" stroke="#22388f" stroke-width="2"/></svg>mark@bnxltd.com</li>
        <li><svg viewBox="0 0 24 24"><circle cx="12" cy="12" r="10"/></svg>www.bnxltd.com</li>
      </ul>
    </div>
    <div class="accent-corner"></div>
    <div class="address-band">
      <svg viewBox="0 0 12 16"><path d="M6 0a6 6 0 0 0-6 6c0 4.5 6 10 6 10s6-5.5 6-10a6 6 0 0 0-6-6zm0 8.5A2.5 2.5 0 1 1 6 3.5a2.5 2.5 0 0 1 0 5z"/></svg>
      Harbour Court, 12 Mill Lane, Leeds, LS2 4PX
    </div>
  </section>

  <section class="card card--back">
    <div class="brand-name">BNX Ltd</div>
  </section>
</body>
</html>
```